Short video intro graphic animation featuring brand mark

I would like a new branded video intro graphic animation to place at the start of the videos I make.
Look at some of the videos on this page for example.
https://www.brackenfieldcup.com/video#!
A more simple one is featured here;
https://www.clipvarno.com/watch?v=Qm7rPbwZ3dN
I would like you use white purple and opacity in the graphic.
My logo is simply the text mark in the attachment.
I would like there to be movement as well. It should be quick.
It can include a sound if you like.
The rest is up to you.

```html
<!DOCTYPE html>
<html lang="en">
<head>
<meta charset="utf-8">
<title>Vote — intro title frame</title>
<link rel="stylesheet" href="https://fonts.googleapis.com/css2?family=Arimo:wght@700&display=swap">
<style>
  :root {
    --brand-purple: #c176b3;
    --mark-white: #f8ebf5;
  }
  html, body {
    margin: 0;
    padding: 0;
    width: 1200px;
    height: 675px;
    overflow: hidden;
    background: var(--brand-purple);
  }
  .intro-stage {
    position: relative;
    width: 1200px;
    height: 675px;
    background: var(--brand-purple);
  }
  .intro-stage svg {
    display: block;
  }
  .wordmark {
    font-family: "Arimo", Arial, sans-serif;
    font-weight: 700;
    font-size: 140px;
    fill: var(--mark-white);
  }
  .letter-settled { opacity: 0.96; }
  .letter-arriving { opacity: 0.85; }
  .letter-trail { opacity: 0.55; }
  .letter-trail-faint { opacity: 0.4; }
  .letter-incoming { opacity: 0.5; }
</style>
</head>
<body>
  <main class="intro-stage">
    <svg width="1200" height="675" viewBox="0 0 1200 675" aria-label="Vote">
      <defs>
        <filter id="motion-light" x="-20%" y="-20%" width="140%" height="140%">
          <feGaussianBlur stdDeviation="3 0.6"/>
        </filter>
        <filter id="motion-strong" x="-30%" y="-20%" width="160%" height="140%">
          <feGaussianBlur stdDeviation="6 1.5"/>
        </filter>
        <filter id="motion-soft" x="-30%" y="-30%" width="160%" height="160%">
          <feGaussianBlur stdDeviation="4 3"/>
        </filter>
      </defs>

      <g class="wordmark">
        <text class="letter-settled" x="696" y="590">Vo</text>

        <text class="letter-trail-faint" x="856" y="590" filter="url(#motion-light)">t</text>
        <text class="letter-arriving" x="868" y="590">t</text>

        <text class="letter-trail" x="902" y="590" filter="url(#motion-strong)">e</text>
        <text class="letter-trail-faint" x="950" y="590" filter="url(#motion-strong)">e</text>

        <text class="letter-incoming" x="1110" y="590" filter="url(#motion-soft)">o</text>
      </g>
    </svg>
  </main>
</body>
</html>
```